Trevolina corporate powerpoint

Hi,
I am creating my own web3 and blockchain academy.

I would like to obtain pricing for a complete corporate powerpoint template for my training sessions in companies and bussiness schools

. I am sharing with you my logo in order to show you my colours.
If you can improve my logo, it will be perfect too. (full pack to launch it)

Thanks
Updates

designers are asiking for an extension

Target Market(s)

Companies and Business Schools

Industry/Entity Type

academy

Font styles to use
Sans Serif
Other font styles liked:
• Arial, Calibri

Colors
0054AA
0677BA
7BADD7
CADEEF
E8F1F8
0094D4
00A9DD
6FCCEA
C7EBF8
E9F6FB
00AB8E
00BBA5
67D7C9
C6EFE9
E9F9F6
F0912C
F2A743
F7CA91
FBE8D2
FDF5EE
EE7325
F08F49
F5BC92
FAE3D3
FDF4ED
6B429C
8869AF
B7A5CE
E3DAEB
F3F0F8

Requirements
Must have
• Blockchain thematic, withe and dark (not black) slides

```html
<!DOCTYPE html>
<html lang="en">
<head>
<meta charset="utf-8">
<title>Trevolina – Corporate Presentation Template</title>
<link rel="stylesheet" href="https://fonts.googleapis.com/css2?family=Montserrat:wght@500;600;700;800&family=Open+Sans:wght@400;600;700&display=swap">
<style>
:root{
  --navy:#0a1c42;
  --navy-deep:#050f2a;
  --blue:#0054AA;
  --sky:#0094D4;
  --cyan:#00A9DD;
  --cyan-soft:#6FCCEA;
  --ice:#E9F6FB;
  --pale:#CADEEF;
  --ink:#1b2a47;
  --muted:#6d7b92;
  --line:#d9e3ee;
  --white:#ffffff;
}
*{box-sizing:border-box;margin:0;padding:0}
html,body{width:1200px;height:3012px;overflow:hidden;background:var(--white)}
body{position:relative;font-family:"Open Sans",Arial,sans-serif;color:var(--ink)}

/* ---------- slide base ---------- */
.slide{position:absolute;width:540px;height:304px;overflow:hidden;background:var(--white);box-shadow:0 2px 10px rgba(10,28,66,.18)}
.slide.dark{background:radial-gradient(ellipse at 70% 40%,#12336e 0%,var(--navy) 45%,var(--navy-deep) 100%);color:var(--white)}
.slide > *{position:absolute}
.col-left{left:48px}.col-right{left:612px}
.row-1{top:800px}.row-2{top:1124px}.row-3{top:1448px}.row-4{top:1772px}.row-5{top:2096px}

.slide-footer{left:0;right:0;bottom:0;height:18px;background:var(--navy);display:flex;align-items:center;justify-content:space-between;padding-left:14px}
.slide-footer .site{font-size:6.5px;color:var(--pale);letter-spacing:.3px}
.slide-footer .page-no{width:34px;height:18px;background:var(--sky);color:var(--white);font-size:7px;font-weight:700;display:flex;align-items:center;justify-content:center}
.slide.dark .slide-footer{background:rgba(0,0,0,.25)}

.slide-title{font-family:"Montserrat",Arial,sans-serif;font-weight:800;font-size:17px;color:var(--navy);letter-spacing:.3px;text-transform:uppercase;white-space:nowrap}
.slide-title .accent{color:var(--sky)}
.title-box{border:2px solid var(--sky);padding:5px 16px;background:var(--white)}
.title-bar{border-left:4px solid var(--sky);padding-left:10px}
.centered{left:50%;transform:translateX(-50%)}
.body-text{font-size:6.2px;line-height:1.5;color:var(--muted)}
.dark .body-text{color:var(--pale)}
.mini-head{font-family:"Montserrat",Arial,sans-serif;font-weight:700;font-size:7px;color:var(--navy);text-transform:uppercase;letter-spacing:.2px}
.dark .mini-head{color:var(--white)}
.image-fill{position:absolute}

/* ---------- brand name ---------- */
.brand{display:flex;align-items:center;gap:7px;font-family:"Montserrat",Arial,sans-serif;font-weight:700;color:var(--white)}
.brand .brand-square{width:12px;height:12px;background:var(--sky)}

/* ---------- cover ---------- */
.cover .brand{left:28px;top:30px;font-size:15px}
.cover .cover-image{left:230px;top:0;width:310px;height:286px;background:radial-gradient(circle at 52% 48%,#6FCCEA 0%,#00A9DD 12%,#0a5aa8 32%,#0b2a63 58%,transparent 80%)}
.cover .cover-title{left:28px;top:98px;font-family:"Montserrat",Arial,sans-serif;font-weight:800;font-size:33px;line-height:1;color:var(--white)}
.cover .cover-sub{left:28px;top:134px;font-family:"Montserrat",Arial,sans-serif;font-weight:600;font-size:15px;color:var(--cyan);letter-spacing:.4px}
.cover .cover-text{left:28px;top:164px;width:210px}
.cover .cover-site{left:0;bottom:14px;width:250px;height:20px;background:var(--sky);display:flex;align-items:center;gap:6px;padding-left:28px;font-size:8px;font-weight:600;color:var(--white)}
.cover .cover-site svg{width:9px;height:9px}
.hero{position:absolute;left:100px;top:110px;transform:scale(1.8519);transform-origin:0 0}

/* ---------- table of contents ---------- */
.toc-grid{left:30px;right:30px;top:82px;display:grid;grid-template-columns:repeat(4,1fr);column-gap:16px;row-gap:26px}
.toc-item{display:flex;gap:6px}
.toc-icon{flex:0 0 16px;height:16px;border:1.5px solid var(--sky);border-radius:50%;display:flex;align-items:center;justify-content:center;font-size:6px;font-weight:700;color:var(--sky)}
.toc-item .mini-head{margin-bottom:3px}

/* ---------- welcome ---------- */
.welcome-band{left:0;top:0;width:40px;height:286px;background:var(--sky)}
.welcome-image{left:22px;top:44px;width:190px;height:150px;background:linear-gradient(135deg,#0b2a63,#0094D4 60%,#6FCCEA)}
.welcome-copy{left:236px;top:36px;width:278px}
.welcome-copy .lead{font-weight:700;font-size:7.5px;color:var(--navy);margin:14px 0 6px}
.welcome-copy .body-text + .body-text{margin-top:6px}

/* ---------- history ---------- */
.history-row{left:24px;right:24px;top:78px;display:grid;grid-template-columns:repeat(4,1fr);gap:12px}
.history-image{height:66px;background:linear-gradient(140deg,#0b2a63,#0677BA 55%,#6FCCEA);margin-bottom:8px}
.history-row .mini-head{color:var(--sky);margin-bottom:3px}

/* ---------- icon features ---------- */
.feature-title{left:24px;top:26px}
.feature-title .slide-title{color:var(--white)}
.feature-grid{left:24px;top:88px;width:220px;display:grid;grid-template-columns:repeat(3,1fr);row-gap:18px}
.feature{text-align:center}
.feature-circle{width:36px;height:36px;margin:0 auto 5px;border-radius:50%;background:var(--sky);display:flex;align-items:center;justify-content:center}
.feature-circle svg{width:16px;height:16px}
.feature .mini-head{font-size:6px}
.feature-image{left:270px;top:24px;width:250px;height:250px;border-radius:50%;background:radial-gradient(circle,#00A9DD 0%,#0a5aa8 35%,#10306b 65%,transparent 72%)}

/* ---------- pie charts ---------- */
.pie-row{left:40px;right:40px;top:80px;display:grid;grid-template-columns:repeat(3,1fr);gap:24px;text-align:center}
.pie-row svg{width:86px;height:86px;display:block;margin:0 auto 10px}
.pie-row .mini-head{margin-bottom:3px}

/* ---------- bar graph ---------- */
.bar-chart{left:24px;top:62px;width:492px;height:210px}

/* ---------- section ---------- */
.section-number{left:30px;top:40px;font-family:"Montserrat",Arial,sans-serif;font-weight:800;font-size:86px;line-height:1;color:rgba(111,204,234,.25)}
.section-name{left:30px;top:140px;font-family:"Montserrat",Arial,sans-serif;font-weight:800;font-size:22px;color:var(--white);white-space:nowrap}
.section-text{left:30px;top:174px;width:190px}
.section-image{left:250px;top:0;width:290px;height:286px;background:linear-gradient(110deg,transparent 0%,#0a3f86 30%,#00A9DD 60%,#0a3f86 85%,transparent 100%)}

/* ---------- table ---------- */
.table-title{left:24px;top:22px}
.table-intro{left:24px;top:54px;width:300px}
.data-table{left:24px;top:82px;width:492px;border-collapse:collapse;font-size:6.5px}
.data-table th{background:var(--navy);color:var(--white);font-weight:700;padding:5px 8px;text-align:left}
.data-table td{padding:4.6px 8px;color:var(--ink);border-bottom:1px solid var(--line)}
.data-table tbody tr:nth-child(odd) td{background:var(--ice)}

/* ---------- cycle diagram ---------- */
.cycle{left:190px;top:66px;width:160px;height:160px}
.cycle-side{top:62px;width:150px;display:flex;flex-direction:column;gap:14px}
.cycle-side.left{left:24px;text-align:right}
.cycle-side.right{left:366px}
.cycle-side .mini-head{font-size:6.2px;margin-bottom:2px}

/* ---------- contact ---------- */
.contact{position:absolute;left:0;top:2420px;width:1200px;height:592px;overflow:hidden;background:linear-gradient(180deg,var(--navy-deep) 0%,var(--navy) 55%,#0b2d66 100%);color:var(--white);text-align:center}
.contact-glow{position:absolute;left:0;right:0;bottom:0;height:300px;background:radial-gradient(ellipse at 50% 100%,#6FCCEA 0%,#00A9DD 18%,#0a4f9c 45%,transparent 75%)}
.contact-watermark{position:absolute;left:0;right:0;top:30px;font-family:"Montserrat",Arial,sans-serif;font-weight:800;font-size:120px;letter-spacing:6px;color:rgba(255,255,255,.05);white-space:nowrap}
.contact .brand{position:absolute;left:50%;top:150px;transform:translateX(-50%);font-size:34px;gap:14px}
.contact .brand .brand-square{width:26px;height:26px}
.contact-details{position:absolute;left:0;right:0;top:228px;font-size:19px;line-height:1.45;font-weight:600}
.social{position:absolute;left:50%;top:338px;transform:translateX(-50%);display:flex;gap:10px}
.social span{width:26px;height:26px;border-radius:50%;background:var(--white)}
.contact-site{position:absolute;left:50%;bottom:36px;transform:translateX(-50%);width:420px;height:44px;border-radius:22px;background:var(--sky);display:flex;align-items:center;justify-content:center;gap:10px;font-size:20px;font-weight:700}
.contact-site svg{width:18px;height:18px}
</style>
</head>
<body>

<!-- hero cover -->
<div class="hero">
  <section class="slide dark cover">
    <div class="cover-image image-fill" role="img" aria-label="Glowing digital padlock on a circuit shield"></div>
    <div class="brand"><span class="brand-square"></span>Trevolina</div>
    <h1 class="cover-title">POWERPOINT</h1>
    <p class="cover-sub">PRESENTATION TITLE</p>
    <p class="cover-text body-text">Lorem Ipsum is simply dummy text of the printing and typesetting industry. Lorem Ipsum has been the standard dummy text ever since, when an unknown printer took a galley of type.</p>
    <div class="cover-site"><svg viewBox="0 0 10 10"><circle cx="5" cy="5" r="4.2" fill="none" stroke="#fff" stroke-width="1"/><path d="M1 5h8M5 .8c-2 2.6-2 5.8 0 8.4M5 .8c2 2.6 2 5.8 0 8.4" fill="none" stroke="#fff" stroke-width=".8"/></svg>www.websiteaddress.com</div>
  </section>
</div>

<!-- row 1 -->
<section class="slide dark cover col-left row-1">
  <div class="cover-image image-fill" role="img" aria-label="Glowing digital padlock on a circuit shield"></div>
  <div class="brand"><span class="brand-square"></span>Trevolina</div>
  <h1 class="cover-title">POWERPOINT</h1>
  <p class="cover-sub">PRESENTATION TITLE</p>
  <p class="cover-text body-text">Lorem Ipsum is simply dummy text of the printing and typesetting industry. Lorem Ipsum has been the standard dummy text ever since, when an unknown printer took a galley of type.</p>
  <div class="cover-site"><svg viewBox="0 0 10 10"><circle cx="5" cy="5" r="4.2" fill="none" stroke="#fff" stroke-width="1"/><path d="M1 5h8M5 .8c-2 2.6-2 5.8 0 8.4M5 .8c2 2.6 2 5.8 0 8.4" fill="none" stroke="#fff" stroke-width=".8"/></svg>www.websiteaddress.com</div>
</section>

<section class="slide col-right row-1">
  <h2 class="slide-title title-box centered" style="top:22px">Table of <span class="accent">Contents</span></h2>
  <div class="toc-grid">
    <div class="toc-item"><span class="toc-icon">01</span><div><p class="mini-head">Heading Text</p><p class="body-text">Lorem ipsum dolor sit amet elit.</p></div></div>
    <div class="toc-item"><span class="toc-icon">02</span><div><p class="mini-head">Heading Text</p><p class="body-text">Lorem ipsum dolor sit amet elit.</p></div></div>
    <div class="toc-item"><span class="toc-icon">03</span><div><p class="mini-head">Heading Text</p><p class="body-text">Lorem ipsum dolor sit amet elit.</p></div></div>
    <div class="toc-item"><span class="toc-icon">04</span><div><p class="mini-head">Heading Text</p><p class="body-text">Lorem ipsum dolor sit amet elit.</p></div></div>
    <div class="toc-item"><span class="toc-icon">05</span><div><p class="mini-head">Heading Text</p><p class="body-text">Lorem ipsum dolor sit amet elit.</p></div></div>
    <div class="toc-item"><span class="toc-icon">06</span><div><p class="mini-head">Heading Text</p><p class="body-text">Lorem ipsum dolor sit amet elit.</p></div></div>
    <div class="toc-item"><span class="toc-icon">07</span><div><p class="mini-head">Heading Text</p><p class="body-text">Lorem ipsum dolor sit amet elit.</p></div></div>
    <div class="toc-item"><span class="toc-icon">08</span><div><p class="mini-head">Heading Text</p><p class="body-text">Lorem ipsum dolor sit amet elit.</p></div></div>
  </div>
  <footer class="slide-footer"><span class="site">www.websiteaddress.com</span><span class="page-no">02</span></footer>
</section>

<!-- row 2 -->
<section class="slide col-left row-2">
  <div class="welcome-band"></div>
  <div class="welcome-image image-fill" role="img" aria-label="Hand touching a glowing blockchain network"></div>
  <div class="welcome-copy">
    <h2 class="slide-title title-bar">Welcome <span class="accent">Message</span></h2>
    <p class="lead">Lorem Ipsum is simply dummy text</p>
    <p class="body-text">Lorem Ipsum is simply dummy text of the printing and typesetting industry. It has been the standard dummy text ever since the sixteenth century.</p>
    <p class="body-text">It has survived not only five centuries, but also the leap into electronic typesetting, remaining essentially unchanged.</p>
    <p class="body-text">It was popularised with the release of sheets containing passages and desktop publishing software.</p>
  </div>
  <footer class="slide-footer"><span class="site">www.websiteaddress.com</span><span class="page-no">03</span></footer>
</section>

<section class="slide col-right row-2">
  <h2 class="slide-title title-box centered" style="top:22px">Our <span class="accent">History</span></h2>
  <div class="history-row">
    <div><div class="history-image" role="img" aria-label="Team working at computers"></div><p class="mini-head">2019</p><p class="body-text">Lorem ipsum dolor sit amet, consectetur elit.</p></div>
    <div><div class="history-image" role="img" aria-label="Digital blockchain cubes"></div><p class="mini-head">2020</p><p class="body-text">Lorem ipsum dolor sit amet, consectetur elit.</p></div>
    <div><div class="history-image" role="img" aria-label="Connected network nodes"></div><p class="mini-head">2021</p><p class="body-text">Lorem ipsum dolor sit amet, consectetur elit.</p></div>
    <div><div class="history-image" role="img" aria-label="Security lock on a circuit board"></div><p class="mini-head">2022</p><p class="body-text">Lorem ipsum dolor sit amet, consectetur elit.</p></div>
  </div>
  <footer class="slide-footer"><span class="site">www.websiteaddress.com</span><span class="page-no">04</span></footer>
</section>

<!-- row 3 -->
<section class="slide dark col-left row-3">
  <div class="feature-title"><h2 class="slide-title title-bar">Heading <span class="accent">Goes Here</span></h2></div>
  <div class="feature-grid">
    <div class="feature"><div class="feature-circle"><svg viewBox="0 0 16 16"><path d="M3 8.5l3 3 7-7" fill="none" stroke="#fff" stroke-width="2"/></svg></div><p class="mini-head">Heading</p></div>
    <div class="feature"><div class="feature-circle"><svg viewBox="0 0 16 16"><rect x="3" y="7" width="10" height="7" fill="none" stroke="#fff" stroke-width="1.6"/><path d="M5 7V5a3 3 0 016 0v2" fill="none" stroke="#fff" stroke-width="1.6"/></svg></div><p class="mini-head">Heading</p></div>
    <div class="feature"><div class="feature-circle"><svg viewBox="0 0 16 16"><rect x="2" y="2" width="5" height="5" fill="none" stroke="#fff" stroke-width="1.5"/><rect x="9" y="9" width="5" height="5" fill="none" stroke="#fff" stroke-width="1.5"/><path d="M7 4.5h4.5V9" fill="none" stroke="#fff" stroke-width="1.5"/></svg></div><p class="mini-head">Heading</p></div>
    <div class="feature"><div class="feature-circle"><svg viewBox="0 0 16 16"><circle cx="8" cy="8" r="5.5" fill="none" stroke="#fff" stroke-width="1.6"/><path d="M8 5v3.5l2.5 1.5" fill="none" stroke="#fff" stroke-width="1.5"/></svg></div><p class="mini-head">Heading</p></div>
    <div class="feature"><div class="feature-circle"><svg viewBox="0 0 16 16"><path d="M2 13l4-4 3 3 5-6" fill="none" stroke="#fff" stroke-width="1.7"/></svg></div><p class="mini-head">Heading</p></div>
    <div class="feature"><div class="feature-circle"><svg viewBox="0 0 16 16"><circle cx="8" cy="6" r="2.6" fill="none" stroke="#fff" stroke-width="1.5"/><path d="M3 14c1-3 9-3 10 0" fill="none" stroke="#fff" stroke-width="1.5"/></svg></div><p class="mini-head">Heading</p></div>
  </div>
  <div class="feature-image image-fill" role="img" aria-label="Circular blockchain network illustration"></div>
  <footer class="slide-footer"><span class="site">www.websiteaddress.com</span><span class="page-no">05</span></footer>
</section>

<section class="slide col-right row-3">
  <h2 class="slide-title title-box centered" style="top:22px">Pie Chart <span class="accent">Goes Here</span></h2>
  <div class="pie-row">
    <div>
      <svg viewBox="0 0 100 100"><circle cx="50" cy="50" r="40" fill="none" stroke="var(--ice)" stroke-width="12"/><circle cx="50" cy="50" r="40" fill="none" stroke="var(--sky)" stroke-width="12" stroke-dasharray="188.5 251.3" transform="rotate(-90 50 50)"/><text x="50" y="55" text-anchor="middle" font-family="Montserrat, sans-serif" font-weight="700" font-size="15" fill="#0a1c42">75%</text></svg>
      <p class="mini-head">Content Heading</p><p class="body-text">Lorem ipsum dolor sit amet elit.</p>
    </div>
    <div>
      <svg viewBox="0 0 100 100"><circle cx="50" cy="50" r="40" fill="none" stroke="var(--ice)" stroke-width="12"/><circle cx="50" cy="50" r="40" fill="none" stroke="var(--blue)" stroke-width="12" stroke-dasharray="150.8 251.3" transform="rotate(-90 50 50)"/><text x="50" y="55" text-anchor="middle" font-family="Montserrat, sans-serif" font-weight="700" font-size="15" fill="#0a1c42">60%</text></svg>
      <p class="mini-head">Content Heading</p><p class="body-text">Lorem ipsum dolor sit amet elit.</p>
    </div>
    <div>
      <svg viewBox="0 0 100 100"><circle cx="50" cy="50" r="40" fill="none" stroke="var(--ice)" stroke-width="12"/><circle cx="50" cy="50" r="40" fill="none" stroke="var(--cyan)" stroke-width="12" stroke-dasharray="125.7 251.3" transform="rotate(-90 50 50)"/><text x="50" y="55" text-anchor="middle" font-family="Montserrat, sans-serif" font-weight="700" font-size="15" fill="#0a1c42">50%</text></svg>
      <p class="mini-head">Content Heading</p><p class="body-text">Lorem ipsum dolor sit amet elit.</p>
    </div>
  </div>
  <footer class="slide-footer"><span class="site">www.websiteaddress.com</span><span class="page-no">06</span></footer>
</section>

<!-- row 4 -->
<section class="slide col-left row-4">
  <h2 class="slide-title title-box" style="left:24px;top:20px">Bar Graph <span class="accent">Goes Here</span></h2>
  <svg class="bar-chart" viewBox="0 0 492 210">
    <g stroke="#d9e3ee" stroke-width="1">
      <line x1="28" y1="10" x2="492" y2="10"/><line x1="28" y1="55" x2="492" y2="55"/><line x1="28" y1="100" x2="492" y2="100"/><line x1="28" y1="145" x2="492" y2="145"/><line x1="28" y1="190" x2="492" y2="190"/>
    </g>
    <g font-family="Open Sans, sans-serif" font-size="7" fill="#6d7b92" text-anchor="end">
      <text x="22" y="13">100</text><text x="22" y="58">75</text><text x="22" y="103">50</text><text x="22" y="148">25</text><text x="22" y="193">0</text>
    </g>
    <g fill="var(--navy)">
      <rect x="44" y="90" width="16" height="100"/><rect x="96" y="60" width="16" height="130"/><rect x="148" y="110" width="16" height="80"/><rect x="200" y="40" width="16" height="150"/><rect x="252" y="80" width="16" height="110"/><rect x="304" y="120" width="16" height="70"/><rect x="356" y="50" width="16" height="140"/><rect x="408" y="95" width="16" height="95"/><rect x="460" y="70" width="16" height="120"/>
    </g>
    <g fill="var(--sky)">
      <rect x="62" y="130" width="16" height="60"/><rect x="114" y="100" width="16" height="90"/><rect x="166" y="140" width="16" height="50"/><rect x="218" y="85" width="16" height="105"/><rect x="270" y="125" width="16" height="65"/><rect x="322" y="150" width="16" height="40"/><rect x="374" y="95" width="16" height="95"/><rect x="426" y="135" width="16" height="55"/><rect x="478" y="115" width="12" height="75"/>
    </g>
    <g font-family="Open Sans, sans-serif" font-size="7" fill="#6d7b92" text-anchor="middle">
      <text x="61" y="203">Jan</text><text x="113" y="203">Feb</text><text x="165" y="203">Mar</text><text x="217" y="203">Apr</text><text x="269" y="203">May</text><text x="321" y="203">Jun</text><text x="373" y="203">Jul</text><text x="425" y="203">Aug</text><text x="475" y="203">Sep</text>
    </g>
  </svg>
  <footer class="slide-footer"><span class="site">www.websiteaddress.com</span><span class="page-no">07</span></footer>
</section>

<section class="slide dark col-right row-4">
  <div class="section-image image-fill" role="img" aria-label="Glowing digital chain links on binary code"></div>
  <p class="section-number">01</p>
  <h2 class="section-name">SECTION SLIDE</h2>
  <p class="section-text body-text">Lorem ipsum dolor sit amet, consectetur adipiscing elit sed do eiusmod.</p>
  <footer class="slide-footer"><span class="site">www.websiteaddress.com</span><span class="page-no">08</span></footer>
</section>

<!-- row 5 -->
<section class="slide col-left row-5">
  <h2 class="slide-title title-bar table-title">Table <span class="accent">Goes Here</span></h2>
  <p class="table-intro body-text">Lorem Ipsum is simply dummy text of the printing and typesetting industry.</p>
  <table class="data-table">
    <thead><tr><th>Description Title</th><th>Title</th><th>Amount</th><th>Percent</th><th>Total</th></tr></thead>
    <tbody>
      <tr><td>Description text</td><td>Text</td><td>$2,400</td><td>24%</td><td>120</td></tr>
      <tr><td>Description text</td><td>Text</td><td>$1,850</td><td>18%</td><td>95</td></tr>
      <tr><td>Description text</td><td>Text</td><td>$3,100</td><td>31%</td><td>160</td></tr>
      <tr><td>Description text</td><td>Text</td><td>$950</td><td>9%</td><td>48</td></tr>
      <tr><td>Description text</td><td>Text</td><td>$1,200</td><td>12%</td><td>62</td></tr>
      <tr><td>Description text</td><td>Text</td><td>$600</td><td>6%</td><td>30</td></tr>
      <tr><td>Description text</td><td>Text</td><td>$700</td><td>7%</td><td>35</td></tr>
    </tbody>
  </table>
  <footer class="slide-footer"><span class="site">www.websiteaddress.com</span><span class="page-no">09</span></footer>
</section>

<section class="slide col-right row-5">
  <h2 class="slide-title title-box centered" style="top:18px">Headline <span class="accent">Goes Here</span></h2>
  <div class="cycle-side left">
    <div><p class="mini-head">Headline Goes Here</p><p class="body-text">Lorem ipsum dolor sit amet elit.</p></div>
    <div><p class="mini-head">Headline Goes Here</p><p class="body-text">Lorem ipsum dolor sit amet elit.</p></div>
    <div><p class="mini-head">Headline Goes Here</p><p class="body-text">Lorem ipsum dolor sit amet elit.</p></div>
  </div>
  <svg class="cycle" viewBox="0 0 160 160">
    <g fill="none" stroke-width="30">
      <circle cx="80" cy="80" r="58" stroke="var(--navy)" stroke-dasharray="57.7 306.7" transform="rotate(-88 80 80)"/>
      <circle cx="80" cy="80" r="58" stroke="var(--blue)" stroke-dasharray="57.7 306.7" transform="rotate(-28 80 80)"/>
      <circle cx="80" cy="80" r="58" stroke="var(--sky)" stroke-dasharray="57.7 306.7" transform="rotate(32 80 80)"/>
      <circle cx="80" cy="80" r="58" stroke="var(--cyan)" stroke-dasharray="57.7 306.7" transform="rotate(92 80 80)"/>
      <circle cx="80" cy="80" r="58" stroke="var(--cyan-soft)" stroke-dasharray="57.7 306.7" transform="rotate(152 80 80)"/>
      <circle cx="80" cy="80" r="58" stroke="#0677BA" stroke-dasharray="57.7 306.7" transform="rotate(212 80 80)"/>
    </g>
    <circle cx="80" cy="80" r="36" fill="var(--ice)"/>
    <text x="80" y="84" text-anchor="middle" font-family="Montserrat, sans-serif" font-weight="800" font-size="11" fill="#0a1c42">TITLE</text>
  </svg>
  <div class="cycle-side right">
    <div><p class="mini-head">Headline Goes Here</p><p class="body-text">Lorem ipsum dolor sit amet elit.</p></div>
    <div><p class="mini-head">Headline Goes Here</p><p class="body-text">Lorem ipsum dolor sit amet elit.</p></div>
    <div><p class="mini-head">Headline Goes Here</p><p class="body-text">Lorem ipsum dolor sit amet elit.</p></div>
  </div>
  <footer class="slide-footer"><span class="site">www.websiteaddress.com</span><span class="page-no">10</span></footer>
</section>

<!-- contact -->
<section class="contact">
  <div class="contact-glow" role="img" aria-label="Glowing city lights seen from above on a curved horizon"></div>
  <p class="contact-watermark">CONTACT US</p>
  <div class="brand"><span class="brand-square"></span>Trevolina</div>
  <div class="contact-details">
    <p>45 Harbour Lane, Northgate 5520</p>
    <p>hello@trevolina-mail.com</p>
    <p>(555) 0142-3300 | (555) 0142-3301</p>
  </div>
  <div class="social"><span></span><span></span><span></span></div>
  <div class="contact-site"><svg viewBox="0 0 10 10"><circle cx="5" cy="5" r="4.2" fill="none" stroke="#fff" stroke-width="1"/><path d="M1 5h8M5 .8c-2 2.6-2 5.8 0 8.4M5 .8c2 2.6 2 5.8 0 8.4" fill="none" stroke="#fff" stroke-width=".8"/></svg>www.websiteaddress.com</div>
</section>

</body>
</html>
```